I'd like a business card that makes my company, Harwick Denton Associates Ltd stand out from the normal financial & IT services sector . It would be great to have a card that a potential client will think "wow" this is out of the norm , I'll give these guys a call. My business aims to provide consultancy services for financial and IT institutions but I'm looking to provide a newer approach that fits into today's social media rather than the standard "big 4" approach. My business helps companies assess their internal issues and aims to solve issues via business process re-engineering. The final design should have a balance of the maturity of the financial & IT sector with the fresh approach of the thriving social media sector

Target Market(s)

Business Managers and Directors, technical Managers and directors. Aged between 20 and 60 that handle project budgets

Industry/Entity Type

Financial

Requirements
Must have
• Must incorporate company logo currently being designed
Should not have
• No old-style fonts please.

```html
<!DOCTYPE html>
<html lang="en">
<head>
<meta charset="utf-8">
<title>Harwick Denton Associates Ltd — Business Card</title>
<link rel="stylesheet" href="https://fonts.googleapis.com/css2?family=Exo+2:wght@400;500;600&display=swap">
<style>
  :root {
    --page-bg: #e6e7ee;
    --card-white: #ffffff;
    --card-grey: #e9eaec;
    --swoosh-dark: #3a3b3f;
    --blue-light: #1f8ddb;
    --blue-deep: #2a4fb0;
    --brand-blue: #2b78d2;
    --text-on-blue: #ffffff;
  }
  html, body {
    margin: 0;
    width: 1200px;
    height: 840px;
    overflow: hidden;
    background: var(--page-bg);
    font-family: "Exo 2", sans-serif;
  }
  .business-card {
    position: absolute;
    left: 75px;
    top: 120px;
    width: 1050px;
    height: 600px;
    overflow: hidden;
    box-shadow: 0 10px 30px rgba(40, 50, 80, 0.18);
  }
  .card-background {
    position: absolute;
    inset: 0;
  }
  .company-name {
    position: absolute;
    left: 42px;
    top: 230px;
    margin: 0;
    font-weight: 600;
    font-size: 44px;
    line-height: 1.05;
    letter-spacing: 2px;
    text-transform: uppercase;
    color: var(--brand-blue);
  }
  .contact-block {
    position: absolute;
    right: 48px;
    top: 70px;
    text-align: right;
    color: var(--text-on-blue);
  }
  .person-name {
    margin: 0;
    font-size: 30px;
    font-weight: 500;
    letter-spacing: 1.5px;
    text-transform: uppercase;
  }
  .person-title {
    margin: 2px 0 0;
    font-size: 18px;
    letter-spacing: 1.5px;
    text-transform: uppercase;
  }
  .address {
    margin: 48px 0 0;
    font-style: normal;
    font-size: 22px;
    line-height: 1.3;
    letter-spacing: 1px;
  }
  .contact-list {
    list-style: none;
    margin: 56px 0 0;
    padding: 0;
    font-size: 21px;
    letter-spacing: 1px;
  }
  .contact-item {
    display: flex;
    justify-content: flex-end;
    align-items: center;
    gap: 12px;
    height: 40px;
  }
  .contact-icon {
    width: 22px;
    height: 22px;
    fill: none;
    stroke: var(--text-on-blue);
    stroke-width: 1.8;
  }
</style>
</head>
<body>
  <section class="business-card">
    <svg class="card-background" viewBox="0 0 1050 600" width="1050" height="600" aria-hidden="true">
      <defs>
        <linearGradient id="paper" x1="0" y1="0" x2="0.6" y2="1">
          <stop offset="0" stop-color="var(--card-white)"/>
          <stop offset="1" stop-color="var(--card-grey)"/>
        </linearGradient>
        <radialGradient id="blue-field" cx="0.8" cy="0.55" r="0.8">
          <stop offset="0" stop-color="var(--blue-light)"/>
          <stop offset="1" stop-color="var(--blue-deep)"/>
        </radialGradient>
      </defs>
      <rect class="paper" width="1050" height="600" fill="url(#paper)"/>
      <path class="swoosh-shadow" d="M762,0 L1050,0 L1050,600 L0,600 L0,512 C440,512 690,260 762,0 Z" fill="var(--swoosh-dark)"/>
      <path class="blue-field" d="M792,0 L1050,0 L1050,600 L0,600 L0,546 C470,540 720,280 792,0 Z" fill="url(#blue-field)"/>
    </svg>

    <h1 class="company-name">Harwick Denton<br>Associates Ltd</h1>

    <div class="contact-block">
      <p class="person-name">Elliot Varga</p>
      <p class="person-title">President</p>
      <address class="address">214, 9th floor, Crest<br>Tower Road HDN</address>
      <ul class="contact-list">
        <li class="contact-item">020 481 7734
          <svg class="contact-icon" viewBox="0 0 24 24"><path d="M5 3h4l2 5-3 2a12 12 0 0 0 6 6l2-3 5 2v4a2 2 0 0 1-2 2A17 17 0 0 1 3 5a2 2 0 0 1 2-2z"/></svg>
        </li>
        <li class="contact-item">020 481 7735
          <svg class="contact-icon" viewBox="0 0 24 24"><rect x="7" y="2" width="10" height="20" rx="2"/><line x1="11" y1="18" x2="13" y2="18"/></svg>
        </li>
        <li class="contact-item">020 481 7736
          <svg class="contact-icon" viewBox="0 0 24 24"><rect x="4" y="9" width="16" height="12" rx="1"/><rect x="8" y="3" width="8" height="6"/><line x1="8" y1="14" x2="16" y2="14"/><line x1="8" y1="17" x2="16" y2="17"/></svg>
        </li>
        <li class="contact-item">hello@harwickdenton.com
          <svg class="contact-icon" viewBox="0 0 24 24"><rect x="3" y="6" width="18" height="12"/><path d="M3 6l9 7 9-7"/></svg>
        </li>
        <li class="contact-item">www.harwickdenton.com
          <svg class="contact-icon" viewBox="0 0 24 24"><circle cx="12" cy="12" r="9"/><ellipse cx="12" cy="12" rx="4" ry="9"/><line x1="3" y1="12" x2="21" y2="12"/></svg>
        </li>
      </ul>
    </div>
  </section>
</body>
</html>
```